New Modern Wix Website Design

We are NOT your typical electrical/home improvement contractor, so we need our website updated. We already have a logo for each division.
We provided a neutral logo with a hard hat, a logo for the home improvement, and a logo for the electrical division. (if we can implement all 3 logos will be great but at least the 2 for the divisions must be used.

We looking for a website that a 10-year-old can understand, our target audience is the new young generation that wants innovations in their properties, smart homes, cool smart things/gadgets. So we need a website that is fun, simple, eye-catching. (we don't want to appear TOO serious and boring)
NO GENERIC WEBSITES SO MUST BE VERY CREATIVE!!!

We want to be able to share google reviews, a contact box, business hours, our services, etc...

current website sirvantelo.us

Target Market(s)

Contractors in different trades.

Industry/Entity Type

Construction

Colors
FFC000
F8CF3A
FAE287
FDF2CF
FEFAEE

Requirements
Must have
• Modern upmarket look and feel
Nice to have
• already attached supporting images.
Should not have
• basic typical construction boring and depressing look and feel.

```html
<!DOCTYPE html>
<html lang="en">
<head>
<meta charset="utf-8">
<title>Open Positions – Mr. Vantelo Electrical Services</title>
<link href="https://fonts.googleapis.com/css2?family=Poppins:wght@400;500;600&display=swap" rel="stylesheet">
<style>
:root{
  --amber:#FFC000;
  --gold:#F8CF3A;
  --butter:#F8E28A;
  --cream:#FCF0CF;
  --ivory:#FEFAEE;
  --ink:#111111;
  --muted:#555555;
  --rule:#b8ad94;
  --logo:#D9961F;
}
*{box-sizing:border-box;margin:0;padding:0}
html,body{width:753px;height:1200px;overflow:hidden;background:#fff;font-family:'Poppins',sans-serif;color:var(--ink)}
.page{position:absolute;left:61.5px;top:24.5px;width:630px;height:1136px;background:var(--cream);overflow:hidden}
.footer-band{position:absolute;left:0;top:800px;width:630px;height:336px}
.abs{position:absolute}
.brand{display:flex;align-items:center;gap:4px;font-weight:600;font-size:8.5px;letter-spacing:.2px;color:var(--ink)}
.brand-dot{width:8px;height:8px;border-radius:50%;background:var(--logo)}
.brand small{display:block;font-size:3.4px;font-weight:500;color:var(--logo);letter-spacing:.6px}
.nav a{position:absolute;top:19px;font-size:7.3px;color:var(--ink);text-decoration:none}
.nav .active{color:#E8A900;border-bottom:1px solid #E8A900}
.dots{position:absolute;top:21px;left:490px;display:flex;gap:2px}
.dots i{width:2.6px;height:2.6px;border-radius:50%;background:var(--ink)}
.btn-contact{position:absolute;left:527.5px;top:13.5px;width:63px;height:19.5px;background:var(--amber);color:#fff;font-size:7.3px;display:flex;align-items:center;justify-content:center}
.hero-art{position:absolute;left:0;top:60.5px;width:127px;height:136px;background:radial-gradient(circle at 40% 50%,#fffdf3 0%,#fdf7e2 70%,var(--cream) 100%);border-radius:0 60% 50% 0/0 50% 55% 0}
.title{position:absolute;left:0;width:630px;top:92px;text-align:center;font-size:20.5px;font-weight:600}
.tag{position:absolute;left:150px;top:128.5px;width:330px;height:18px;background:var(--gold);font-size:10px;font-weight:600;display:flex;align-items:center;justify-content:center}
.section-head{position:absolute;left:132.5px;width:365px;display:flex;align-items:center;gap:6px;font-size:10.3px;font-weight:600;border-bottom:1px solid var(--rule);padding-bottom:8px}
.section-head svg{width:22px;height:22px;flex:none}
.copy{position:absolute;left:132.5px;top:227px;width:370px;font-size:7.3px;line-height:11.2px}
.label{position:absolute;font-size:7.6px;font-weight:600}
.field{position:absolute;height:16.3px;border:1px solid #333;border-radius:3px;background:#fff;font-size:5.6px;color:var(--muted);padding-left:12.5px;display:flex;align-items:center}
.field.dark{color:#222}
.chev{position:absolute;right:7px;top:4px}
.question{position:absolute;left:132.5px;top:563px;font-size:5.8px;color:#222}
.question b{color:#e23;font-weight:400}
.radio{position:absolute;left:132.5px;font-size:5.8px;display:flex;align-items:center;gap:3.5px}
.radio i{width:6px;height:6px;border:1px solid #444;border-radius:50%}
.area{position:absolute;left:132.5px;top:601px;width:365px;height:60px;border:1px solid #333;border-radius:3px;background:#fff;font-size:5.6px;color:#222;padding:6px 12.5px}
.submit{position:absolute;left:132.5px;top:684px;width:365px;height:23px;background:#000;color:#fff;font-size:7.3px;font-weight:600;display:flex;align-items:center;justify-content:center}
.newsletter{position:absolute;left:86.5px;top:756px;width:457px;height:115px;background:var(--butter);border-radius:6px;box-shadow:0 2px 6px rgba(180,150,60,.18)}
.newsletter h2{position:absolute;width:100%;top:14px;text-align:center;font-size:20px;font-weight:600}
.newsletter p{position:absolute;width:100%;top:47px;text-align:center;font-size:7.3px;font-weight:500}
.nl-input{position:absolute;left:39.5px;top:64.5px;width:180px;height:30px;background:#fff;font-size:5.8px;color:#999;display:flex;align-items:center;padding-left:13px}
.nl-btn{position:absolute;left:237px;top:64.5px;width:180px;height:30px;background:var(--amber);font-size:7.3px;font-weight:600;display:flex;align-items:center;justify-content:center}
.foot-h{position:absolute;top:975px;font-size:9.8px;font-weight:600}
.foot-list{position:absolute;top:1000px;list-style:none;font-size:7.4px;line-height:17px}
.square{position:absolute;left:217.5px;top:1073px;width:8px;height:8px;background:var(--amber)}
.map{position:absolute;left:410.5px;top:1005.5px;width:179.5px;height:98px;background:linear-gradient(135deg,#ece8e0,#e6dfcf 55%,#dfe6d8)}
.copyright{position:absolute;left:0;width:630px;top:1116px;text-align:center;font-size:5.2px;color:#444}
</style>
</head>
<body>
<div class="page">
  <svg class="footer-band" viewBox="0 0 630 336" preserveAspectRatio="none" aria-hidden="true">
    <path d="M0 30 C150 0 480 0 630 22 L630 336 L0 336 Z" fill="#FEFAEE"/>
  </svg>

  <div class="abs brand" style="left:40px;top:33px">
    <span class="brand-dot"></span>
    <span>MR. VANTELO<small>ELECTRICAL SERVICES</small></span>
  </div>

  <nav class="nav">
    <a style="left:258px">Home</a>
    <a style="left:300px">Our Services</a>
    <a class="active" style="left:367px">Job Opportunity</a>
    <a style="left:447.5px">About</a>
    <span class="dots"><i></i><i></i><i></i></span>
  </nav>
  <div class="btn-contact">Contact us</div>

  <div class="hero-art" role="img" aria-label="Illustration of a hand writing on a document beside a coffee cup"></div>

  <h1 class="title">Open Positions</h1>
  <div class="tag">Independent Journeyman Electricians and Apprentice/Helpers</div>

  <div class="section-head" style="top:185px">
    <svg viewBox="0 0 22 22" aria-hidden="true"><rect x="3" y="2" width="13" height="17" rx="1" fill="#FDF2CF" stroke="#333" stroke-width=".8"/><path d="M6 7h7M6 10h7M6 13h5" stroke="#333" stroke-width=".7"/><path d="M13 20l7-9" stroke="#F8CF3A" stroke-width="1.6"/></svg>
    Description
  </div>
  <div class="copy">
    <p>Mr. Vantelo is hiring Independent Journeyman Electricians, with at least 5 years of experience in both residential and commercial.<br>Pays up to $120k a year.</p>
    <p style="margin-top:11px">To begin the application, please fill out the form below and include as much detail as possible for consideration. We’ll contact you with any questions and/or to schedule an interview.</p>
  </div>

  <div class="section-head" style="top:311px">
    <svg viewBox="0 0 22 22" aria-hidden="true"><rect x="2" y="3" width="14" height="13" rx="1" fill="#FDF2CF" stroke="#333" stroke-width=".8"/><circle cx="15" cy="15" r="4" fill="#fff" stroke="#333" stroke-width=".8"/><path d="M18 18l3 3" stroke="#333" stroke-width="1"/></svg>
    personal Information
  </div>
  <span class="label" style="left:132.5px;top:355px">First name</span>
  <span class="label" style="left:329.5px;top:355px">Last name</span>
  <div class="field" style="left:132.5px;top:368.5px;width:168px">John</div>
  <div class="field" style="left:329.5px;top:368.5px;width:168px">Doe</div>
  <span class="label" style="left:132.5px;top:392px">Email</span>
  <div class="field" style="left:132.5px;top:405.5px;width:365px">Johndoe@mailbox.com</div>
  <span class="label" style="left:132.5px;top:429px">Phone number</span>
  <div class="field" style="left:132.5px;top:442.5px;width:365px">033 456784</div>

  <div class="section-head" style="top:474px">
    <svg viewBox="0 0 22 22" aria-hidden="true"><rect x="5" y="2" width="13" height="17" rx="1" fill="#FDF2CF" stroke="#333" stroke-width=".8"/><rect x="8" y="6" width="7" height="5" fill="none" stroke="#333" stroke-width=".6"/><path d="M2 20l6-7" stroke="#333" stroke-width="1.2"/></svg>
    Details
  </div>
  <div class="field dark" style="left:132.5px;top:517px;width:365px">Select Your Job position
    <svg class="chev" width="8" height="6" viewBox="0 0 8 6" aria-hidden="true"><path d="M1 2l3 2.5L7 2" fill="none" stroke="#111" stroke-width="1"/></svg>
  </div>
  <div class="field dark" style="left:132.5px;top:540.5px;width:365px">How many years of experience you have for this type of job?</div>
  <p class="question">Are you acrophobic? (afraid of heights)<b>*</b></p>
  <label class="radio" style="top:577px"><i></i>Yes</label>
  <label class="radio" style="top:586.5px"><i></i>No</label>
  <div class="area">Do you have any additional details</div>
  <div class="submit">SUBMIT</div>

  <section class="newsletter">
    <h2>Join Our Newslatter</h2>
    <p>Join to get our news as we publish them</p>
    <div class="nl-input">John@mailbox.com</div>
    <div class="nl-btn">SIGN UP</div>
  </section>

  <div class="abs brand" style="left:40px;top:918px">
    <span class="brand-dot"></span>
    <span>MR. VANTELO<small>ELECTRICAL SERVICES</small></span>
  </div>

  <h3 class="foot-h" style="left:40px">Quick Links</h3>
  <h3 class="foot-h" style="left:217.5px">Contact us</h3>
  <h3 class="foot-h" style="left:410.5px">Our Locations</h3>
  <ul class="foot-list" style="left:40px">
    <li>Home</li><li>Our Services</li><li>Job Opportunity</li><li>About</li>
  </ul>
  <ul class="foot-list" style="left:217.5px">
    <li>info@sirvantelo.us</li><li>P +1 (833) 555-0148</li><li>F +1 (833) 555-0148</li><li>Brookfield, PA 17000</li>
  </ul>
  <span class="square"></span>
  <div class="map" role="img" aria-label="Street map showing the company location"></div>
  <p class="copyright">©2021 by Mr. Vantelo ®</p>
</div>
</body>
</html>
```